■書籍タイトル
「町工房・路地の店・士業のための、明日効く集客設計術・KRT」

・堅苦しくなく、わかりやすいイメージにしたいです
・電子書籍なので、画像が小さいので、できるだけ視認しやすい文字でお願いします

■オビ
「お金も時間もかけずに、たった2つのことをするだけで、ライバルが歯ぎしりするほどお客に選ばれる」

■著者  森野沙知絵
■発行  東陽商務文化出版舎

■色の指定などはありません。お任せです。
(明るい・カンタン・わかりやすい)
イメージイラストなど入ってもよいかと思います。

■高級感やアカデミックより、明るくカンタンなイメージで。

※参考資料として、書籍の原稿と、同じタイトルのセミナーのパワポ表紙画像を添付します。
アカデミックな感じより、ポップな感じや明るいイメージ、
「わかりやすさ」「文字の視認性」を重視します。
クラフターのみなさま、
引き続き、ご提案をお待ちしております。
みなさま、ご提案ありがとうございます。

中小企業・小さなお店・先生業
という文字が小さい表示のデザインが多いのですが、

ターゲット層が一目で見てわかるよう、

中小企業・小さなお店・先生業

という文字が見えるようにしたいです。

引き続き、みなさまからのご提案をお待ちしております。
たくさんのご提案をいただきありがとうございます。

本のタイトルが、変更となりました。
金額をアップし、締め切りを1日延長いたしますので、
訂正ご対応いただければ幸いです。

新しいタイトルは、

「中小企業・小さなお店・先生業が
常連が増え続けるために明日から始める三つの習慣」
です。

帯、またはサブタイトルは、
「ライバルが歯ぎしりするほどお客が押し寄せる新時代の差別化戦略」
としてください。

ご提案をお待ちしております。
よろしくお願いいたします。

今回の装丁は、特に「わかりやすさ」を重視しておりました。
レベルの高い装丁デザインが多く、選考に大変迷いました。
選定させていただきましたデザインは、笑顔の3職種の人物のイラストと、フォントの使い方など、わかりやすい・明るい・カンタンという目指すところをこちらの想定以上に表現していただいたことが一番の理由です。

たくさんのご提案をいただき、ありがとうございました。
本当にレベルの高いデザインが多く選定では社内でも意見が割れました。
また、再三の追記・変更によりお手数をおかけしましたことを、この場を借りてお詫び申し上げます。

今後も定期的に装丁の依頼をいたしますので、どうぞよろしくお願いいたします。

```html
<!DOCTYPE html>
<html lang="ja">
<head>
<meta charset="utf-8">
<title>明日効く集客設計術 KRT</title>
<link rel="stylesheet" href="https://fonts.googleapis.com/css2?family=Noto+Sans+JP:wght@700;900&family=Noto+Serif+JP:wght@500;600&display=swap">
<style>
  :root {
    --paper: #ffffff;
    --ink: #141414;
    --accent: #ec8a1f;
    --hand-light: #e6eaef;
    --hand-dark: #aab4bf;
  }
  * { margin: 0; padding: 0; box-sizing: border-box; }
  html, body { width: 749px; height: 1200px; overflow: hidden; background: var(--paper); }
  .cover {
    position: relative; width: 749px; height: 1200px; overflow: hidden;
    background: var(--paper); color: var(--ink);
    font-family: "Noto Sans JP", sans-serif;
  }
  .accent-band {
    position: absolute; left: 0; top: 930px; width: 749px; height: 210px;
    background: var(--accent);
  }
  .target {
    position: absolute; top: 26px; width: 100%; text-align: center;
    font-weight: 900; font-size: 40px; letter-spacing: 1px; line-height: 1.3;
  }
  .particle {
    position: absolute; left: 462px; top: 88px;
    color: var(--accent); font-weight: 900; font-size: 28px; line-height: 1;
  }
  .subtitle {
    position: absolute; top: 114px; width: 100%; text-align: center;
    font-weight: 900; font-size: 60px; letter-spacing: 2px; line-height: 1.2;
  }
  .acronym {
    position: absolute; top: 212px; left: 0; width: 100%;
    display: flex; justify-content: center; gap: 50px;
  }
  .acronym .letter {
    display: flex; flex-direction: column; align-items: center; width: 170px;
  }
  .acronym .gloss {
    color: var(--accent); font-weight: 700; font-size: 20px; letter-spacing: 2px; line-height: 1.2;
  }
  .acronym .mark {
    font-family: "Noto Serif JP", serif; font-weight: 500;
    font-size: 140px; line-height: 1; margin-top: 2px;
  }
  .author {
    position: absolute; top: 408px; width: 100%; text-align: center;
    font-family: "Noto Serif JP", serif; font-weight: 500;
    font-size: 100px; letter-spacing: 4px; line-height: 1.1;
  }
  .illustration {
    position: absolute; left: 215px; top: 575px; width: 220px; height: 340px;
  }
  .pitch { position: absolute; inset: 0; }
  .pitch span {
    position: absolute; writing-mode: vertical-rl; text-orientation: upright;
    font-weight: 900; font-size: 52px; line-height: 1; letter-spacing: 2px; white-space: nowrap;
  }
  .pitch .small-accent { color: var(--accent); font-size: 30px; }
  .pitch .big-accent { color: var(--accent); font-size: 100px; }
  .publisher {
    position: absolute; top: 1150px; width: 100%; text-align: center;
    font-weight: 700; font-size: 28px; letter-spacing: 1px; line-height: 1.3;
  }
</style>
</head>
<body>
<main class="cover">
  <div class="accent-band"></div>

  <p class="target">町工房・路地の店・士業のための</p>
  <span class="particle">の</span>
  <h2 class="subtitle">明日効く集客設計術</h2>

  <h1 class="acronym">
    <span class="letter"><span class="gloss">コミュニティ</span><span class="mark">K</span></span>
    <span class="letter"><span class="gloss">リピート</span><span class="mark">R</span></span>
    <span class="letter"><span class="gloss">トラスト</span><span class="mark">T</span></span>
  </h1>

  <p class="author">森野沙知絵</p>

  <svg class="illustration" role="img" aria-label="ピースサインをする手のイラスト" viewBox="0 0 220 340">
    <defs>
      <linearGradient id="handTone" x1="0" y1="0" x2="1" y2="1">
        <stop offset="0" stop-color="var(--hand-light)"/>
        <stop offset="1" stop-color="var(--hand-dark)"/>
      </linearGradient>
    </defs>
    <rect x="0" y="0" width="220" height="340" rx="80" fill="url(#handTone)" opacity="0.6"/>
  </svg>

  <p class="pitch">
    <span style="left:682px; top:820px;">お金も時間も</span>
    <span style="left:606px; top:862px;">かけずに、</span>
    <span class="small-accent" style="left:566px; top:578px;">たった</span>
    <span class="big-accent" style="left:456px; top:590px;">2つ</span>
    <span style="left:480px; top:812px;">のことを</span>
    <span style="left:405px; top:700px;">するだけで、</span>
    <span style="left:332px; top:628px;">ライバルが</span>
    <span style="left:256px; top:590px;">歯ぎしりするほど</span>
    <span style="left:180px; top:752px;">お客に選ばれる</span>
  </p>

  <p class="publisher">東陽商務文化出版舎</p>
</main>
</body>
</html>
```